Business Card Design

Company name is: Tallowmere Rescue Skills, LLC. We teach CPR/AED, First Aid, Bloodborne Pathogens and other health and safety classes. Looking for an eye-catching, progressive, cutting edge design.

Industry/Entity Type

Health

Contact Information for Business Card

Dale Fenwarick (555.218.4703)
Nora Quillstead (555.276.9148)
email is info@tallowmererescue.example
website is www.TallowmereRescue.example

```html
<!DOCTYPE html>
<html lang="en">
<head>
<meta charset="utf-8">
<title>Tallowmere Rescue Skills, LLC — Business Card</title>
<link rel="stylesheet" href="https://fonts.googleapis.com/css2?family=Open+Sans:wght@400;600&family=Libre+Baskerville:wght@700&display=swap">
<style>
  :root {
    --stage: #3a3340;
    --card: #ffffff;
    --navy: #252a7e;
    --navy-deep: #1c2068;
    --salmon: #f28f8c;
    --white: #ffffff;
    --rule: rgba(255,255,255,0.75);
    --red: #e8232b;
    --ink: #161616;
  }
  html, body {
    margin: 0;
    padding: 0;
    width: 1200px;
    height: 800px;
    overflow: hidden;
    background: var(--stage);
  }
  .canvas {
    position: relative;
    width: 1200px;
    height: 800px;
  }
  .card {
    position: absolute;
    left: 100px;
    top: 114px;
    width: 1000px;
    height: 572px;
    background: var(--card);
    overflow: hidden;
    box-shadow: 0 14px 40px rgba(0,0,0,0.35);
  }
  .card-art {
    position: absolute;
    inset: 0;
  }
  .contacts {
    position: absolute;
    left: 90px;
    top: 56px;
    width: 360px;
    font-family: "Open Sans", sans-serif;
    color: var(--white);
  }
  .person-name {
    font-size: 28px;
    color: var(--salmon);
    line-height: 1.1;
    margin: 0;
  }
  .contact-line {
    display: flex;
    align-items: center;
    gap: 10px;
    font-size: 21px;
    line-height: 1.35;
    margin: 0;
    white-space: nowrap;
  }
  .contact-line.small { font-size: 18px; line-height: 1.5; }
  .contact-line svg { flex: none; }
  .divider {
    height: 1px;
    background: var(--rule);
    margin: 12px 0 16px;
    width: 340px;
  }
  .brand {
    position: absolute;
    left: 500px;
    top: 330px;
  }
  .brand-name {
    display: flex;
    align-items: center;
    gap: 12px;
    font-family: "Libre Baskerville", serif;
    font-weight: 700;
    font-size: 20px;
    color: var(--ink);
    letter-spacing: 0.3px;
    margin: 0;
    white-space: nowrap;
  }
  .brand-dot {
    width: 14px;
    height: 14px;
    border-radius: 50%;
    background: var(--red);
  }
  .tagline {
    font-family: "Open Sans", sans-serif;
    font-size: 17px;
    color: var(--red);
    margin: 8px 0 0 26px;
    line-height: 1.35;
  }
  .tagline span { display: block; white-space: nowrap; }
  .tagline span + span { padding-left: 14px; }
</style>
</head>
<body>
<div class="canvas">
  <div class="card">
    <svg class="card-art" width="1000" height="572" viewBox="0 0 1000 572">
      <defs>
        <linearGradient id="navyFill" x1="0" y1="0" x2="1" y2="1">
          <stop offset="0" stop-color="#2c3190"/>
          <stop offset="1" stop-color="#1c2068"/>
        </linearGradient>
      </defs>
      <path class="navy-panel" d="M0 0 H600 C590 330 380 510 0 548 Z" fill="url(#navyFill)"/>
      <polyline class="pulse-line" fill="none" stroke="#e8232b" stroke-width="3" stroke-linejoin="round"
        points="250,488 320,488 330,472 340,510 352,450 364,502 372,488 1000,488"/>
    </svg>

    <div class="contacts">
      <p class="person-name">Dale Fenwarick</p>
      <p class="contact-line">
        <svg width="16" height="18" viewBox="0 0 16 18"><path d="M3 1 L6 1 L7 5 L5 7 C6 10 8 12 10 13 L12 11 L15 12 L15 15 C15 16 14 17 13 17 C6 16 1 10 1 3 C1 2 2 1 3 1 Z" fill="#fff"/></svg>
        555.218.4703
      </p>
      <div class="divider"></div>
      <p class="person-name">Nora Quillstead</p>
      <p class="contact-line">
        <svg width="16" height="18" viewBox="0 0 16 18"><path d="M3 1 L6 1 L7 5 L5 7 C6 10 8 12 10 13 L12 11 L15 12 L15 15 C15 16 14 17 13 17 C6 16 1 10 1 3 C1 2 2 1 3 1 Z" fill="#fff"/></svg>
        555.276.9148
      </p>
      <div class="divider"></div>
      <p class="contact-line small">
        <svg width="18" height="14" viewBox="0 0 18 14"><rect x="1" y="1" width="16" height="12" fill="none" stroke="#fff" stroke-width="1.6"/><polyline points="1,1 9,8 17,1" fill="none" stroke="#fff" stroke-width="1.6"/></svg>
        info@tallowmererescue.example
      </p>
      <p class="contact-line small">
        <svg width="18" height="18" viewBox="0 0 18 18"><circle cx="9" cy="9" r="8" fill="#fff"/><path d="M5 5 C7 6 7 9 5 11 M12 4 C10 7 11 10 14 12" stroke="#252a7e" stroke-width="1.6" fill="none"/></svg>
        www.TallowmereRescue.example
      </p>
    </div>

    <div class="brand">
      <p class="brand-name"><span class="brand-dot"></span>TALLOWMERE RESCUE SKILLS, LLC</p>
      <p class="tagline">
        <span>CPR/AED, First Aid, Bloodborne Pathogens</span>
        <span>and other health and safety classes</span>
      </p>
    </div>
  </div>
</div>
</body>
</html>
```